Brintell's Business Card

I need some designs for a new business card including the new logo attached. An old example of our business card is also attached to show all the data that should be included on the new design.
**I added some more examples someone had mocked up**

Contact Information for Business Card

Should include all info on other examples uploaded.

```html
<!DOCTYPE html>
<html lang="en">
<head>
<meta charset="utf-8">
<title>Brintell's Business Card</title>
<link href="https://fonts.googleapis.com/css2?family=Montserrat:wght@500;600;700;800&family=Mulish:wght@400;500;600&display=swap" rel="stylesheet">
<style>
  :root {
    --bg: #5f6061;
    --paper: #f7f7f7;
    --brand-blue: #2b7fd0;
    --band-blue: #2e8ad6;
    --deep-blue: #3a4db0;
    --accent-red: #e8383d;
    --ink: #1d1d1f;
    --white: #ffffff;
  }
  * { box-sizing: border-box; margin: 0; padding: 0; }
  html, body { width: 1200px; height: 910px; overflow: hidden; }
  body {
    background: var(--bg);
    display: flex;
    flex-direction: column;
    align-items: center;
    justify-content: center;
    gap: 50px;
    font-family: "Mulish", sans-serif;
  }
  .card {
    position: relative;
    width: 700px;
    height: 400px;
    overflow: hidden;
    box-shadow: 0 10px 24px rgba(0,0,0,0.35);
  }
  .card--front { background: var(--paper); }
  .card--back { background: var(--deep-blue); }

  .card__decor {
    position: absolute;
    top: 0;
    right: 0;
    width: 230px;
    height: 300px;
  }
  .card__band {
    position: absolute;
    left: 0;
    bottom: 0;
    width: 700px;
    height: 140px;
  }
  .card__band-text {
    position: absolute;
    left: 40px;
    bottom: 16px;
    font-size: 17px;
    font-weight: 500;
    color: var(--white);
    letter-spacing: 0.2px;
  }

  .brand {
    position: absolute;
    display: flex;
    align-items: center;
    gap: 12px;
  }
  .brand__dot {
    width: 16px;
    height: 16px;
    border-radius: 50%;
    background: var(--accent-red);
    flex: none;
  }
  .brand__name {
    font-family: "Montserrat", sans-serif;
    font-weight: 700;
    font-size: 46px;
    line-height: 1;
    letter-spacing: 1px;
  }
  .brand__tagline {
    font-family: "Montserrat", sans-serif;
    font-weight: 600;
    font-size: 12.5px;
    color: var(--accent-red);
    letter-spacing: 0.4px;
    margin-top: 5px;
  }
  .card--front .brand { left: 46px; top: 82px; }
  .card--front .brand__name { color: var(--brand-blue); }
  .card--back .brand { left: 60px; top: 100px; }
  .card--back .brand__name { color: var(--white); }

  .front__rule {
    position: absolute;
    left: 46px;
    top: 172px;
    width: 430px;
    height: 2px;
    background: var(--accent-red);
  }
  .front__rule::after {
    content: "";
    position: absolute;
    right: -5px;
    top: -4px;
    width: 10px;
    height: 10px;
    border-radius: 50%;
    background: var(--accent-red);
  }
  .contact {
    position: absolute;
    left: 46px;
    top: 190px;
  }
  .contact__name {
    font-family: "Montserrat", sans-serif;
    font-weight: 700;
    font-size: 30px;
    color: var(--accent-red);
    padding-bottom: 6px;
    border-bottom: 2px solid var(--accent-red);
    display: inline-block;
    padding-right: 14px;
  }
  .contact__line {
    display: flex;
    align-items: center;
    gap: 8px;
    font-size: 20px;
    color: var(--ink);
    margin-top: 10px;
  }
  .contact__line svg { flex: none; }

  .back__pitch {
    position: absolute;
    left: 88px;
    top: 186px;
    font-size: 22px;
    line-height: 1.25;
    color: var(--white);
    font-weight: 500;
  }
</style>
</head>
<body>

  <section class="card card--front" aria-label="Business card front">
    <svg class="card__decor" viewBox="0 0 230 300" role="img" aria-label="Large flame-and-drop brand decoration in red and blue">
      <defs>
        <linearGradient id="decorFront" x1="0" y1="0" x2="1" y2="1">
          <stop offset="0" stop-color="#e8383d" stop-opacity="0.85"/>
          <stop offset="1" stop-color="#2e8ad6" stop-opacity="0.85"/>
        </linearGradient>
      </defs>
      <rect width="230" height="300" fill="url(#decorFront)"/>
    </svg>

    <div class="brand">
      <span class="brand__dot"></span>
      <div>
        <div class="brand__name">BRINTELL'S</div>
        <div class="brand__tagline">AIR CONDITIONING &amp; HEATING SERVICE</div>
      </div>
    </div>

    <div class="front__rule"></div>

    <div class="contact">
      <div class="contact__name">Dale Brintell</div>
      <div class="contact__line">
        <svg width="16" height="16" viewBox="0 0 24 24"><path fill="#e8383d" d="M6.6 10.8a15.1 15.1 0 0 0 6.6 6.6l2.2-2.2c.3-.3.7-.4 1-.2 1.1.4 2.3.6 3.6.6.6 0 1 .4 1 1V20c0 .6-.4 1-1 1A17 17 0 0 1 3 4c0-.6.4-1 1-1h3.5c.6 0 1 .4 1 1 0 1.3.2 2.5.6 3.6.1.3 0 .7-.2 1z"/></svg>
        555.014.2290
      </div>
      <div class="contact__line">
        <svg width="16" height="16" viewBox="0 0 24 24"><path fill="#e8383d" d="M2 5h20v14H2z"/><path fill="none" stroke="#fff" stroke-width="2" d="M3 6l9 7 9-7"/></svg>
        brintellhvac@mailbox.com
      </div>
    </div>

    <svg class="card__band" viewBox="0 0 700 140" aria-hidden="true">
      <path fill="#2e8ad6" d="M0 100 L470 100 C540 100 560 40 620 30 C660 24 690 20 700 20 L700 140 L0 140 Z"/>
    </svg>
    <div class="card__band-text">Licensed &amp; Insured Family Owned &amp; Operated</div>
  </section>

  <section class="card card--back" aria-label="Business card back">
    <svg class="card__decor" viewBox="0 0 230 300" role="img" aria-label="Large flame-and-drop brand decoration in red and pale blue">
      <defs>
        <linearGradient id="decorBack" x1="0" y1="0" x2="1" y2="1">
          <stop offset="0" stop-color="#e8383d" stop-opacity="0.9"/>
          <stop offset="1" stop-color="#a9b0ea" stop-opacity="0.8"/>
        </linearGradient>
      </defs>
      <rect width="230" height="300" fill="url(#decorBack)"/>
    </svg>

    <div class="brand">
      <span class="brand__dot"></span>
      <div>
        <div class="brand__name">BRINTELL'S</div>
        <div class="brand__tagline">AIR CONDITIONING &amp; HEATING SERVICE</div>
      </div>
    </div>

    <p class="back__pitch">Call today for all your hvac,<br>refrigeration &amp; plumbing needs</p>

    <svg class="card__band" viewBox="0 0 700 140" aria-hidden="true">
      <path fill="#2e8ad6" d="M0 100 L470 100 C540 100 560 40 620 30 C660 24 690 20 700 20 L700 140 L0 140 Z"/>
    </svg>
    <div class="card__band-text">Serves Maplecrest, IA &amp; Surrounding Areas</div>
  </section>

</body>
</html>
```